Calm Meadowline Company Profile

We have all the written content for our company profile and just need the background graphics and layout designed, this can be seen at our website www.calm-meadowline.example or in the attached company profiles
We are happy with the content as far as wording and our logo are concerned, we are looking to revamp the background and layout.
The intention is for this to be printed as a brochure where the inside of the rear page has a pocket at the bottom so that our relevant affiliated companies brochures can be inserted into to complete the package depending on who we are presenting it to.

Target Market(s)

Oil & Gas, Power Generation, Mining, Maritime, Marine, Automation, Engineering

Industry/Entity Type

Engineering Consulting

Colors

Designer to choose colors to be used in the design.

Requirements
Must have
• Existing provided content
Nice to have
• engineering background and images that pop
Should not have
• our target market is Oil & Gas, Power Generation, Mining, Maritime, Marine, Automation, Engineering so it should not have content that does not relate to these industries

```html
<!DOCTYPE html>
<html lang="en">
<head>
<meta charset="utf-8">
<title>Calm Meadowline – Company Profile Spread</title>
<link href="https://fonts.googleapis.com/css2?family=Roboto:wght@300;400;500;700&display=swap" rel="stylesheet">
<style>
:root{
  --teal:#3bb8c0;
  --teal-dark:#1f8e98;
  --ink:#3a3a3a;
  --ink-soft:#6b6b6b;
  --paper:#ffffff;
  --stage:#e8e9ea;
}
*{box-sizing:border-box;margin:0;padding:0}
html,body{width:1200px;height:1200px;overflow:hidden}
body{background:var(--stage);font-family:"Roboto",sans-serif;color:var(--ink);position:relative}
.spread{position:absolute;left:0;top:390px;width:1200px;height:420px;background:var(--paper);display:flex;box-shadow:0 2px 10px rgba(0,0,0,.12)}
.panel{position:relative;width:300px;height:420px;overflow:hidden}
.ph{position:absolute}
.small{font-size:5px;line-height:1.3;font-weight:400;text-align:justify;color:var(--ink)}
.small p{margin-bottom:2px}
.h-teal{color:var(--teal-dark);font-weight:500}

/* panel 1 */
.map{left:15px;top:6px;width:225px;height:118px;background:linear-gradient(180deg,#2aa6b0,#1f8e98);border-radius:4px}
.projects-title{position:absolute;left:18px;top:139px;font-size:6.8px;font-weight:500;color:var(--teal-dark)}
.projects{position:absolute;left:18px;top:151px;width:268px;list-style:none;font-size:5.3px;line-height:1.42}
.projects li{margin-bottom:4px}
.projects li::before{content:"• ";color:var(--teal)}
.contact{position:absolute;left:18px;top:313px;font-size:5px;line-height:1.55;color:var(--ink)}
.contact .h-teal{font-size:5.8px;display:block;margin-bottom:1px}
.badges{position:absolute;left:18px;top:361px;display:flex;gap:4px}
.badges span{width:28px;height:30px;background:#24466f;display:block}
.badges span+span{background:#1d3a62}

/* panel 2 */
.rig{left:0;top:0;width:300px;height:150px;background:linear-gradient(180deg,#9cc6e4 0%,#d7e7f2 48%,#e0a640 62%,#3f6f94 78%,#24537a 100%)}
.rule{position:absolute;left:0;top:160px;width:300px;height:4px;background:var(--teal)}
.services{position:absolute;top:178px;list-style:none;font-size:7.2px;line-height:1.32;color:var(--teal-dark)}
.services li::before{content:"› ";font-weight:700}
.svc-a{left:16px}.svc-b{left:110px;width:190px}
.strip{position:absolute;top:246px;left:0;width:300px;height:98px;display:flex;gap:2px}
.strip div{flex:1}
.s1{background:linear-gradient(180deg,#6d7ea6,#e08a55 60%,#3a3446)}
.s2{background:linear-gradient(180deg,#e7b26a,#c56a3c 55%,#2e2a2c)}
.s3{background:linear-gradient(180deg,#7d8fb3,#e3a25e 60%,#2f2f38)}
.brand{position:absolute;left:93px;top:370px;display:flex;align-items:center;gap:6px}
.brand i{width:14px;height:14px;background:var(--teal);display:block}
.brand b{font-size:17px;font-weight:700;color:var(--ink-soft);letter-spacing:.2px}

/* panel 3 */
.swoop{position:absolute;right:0;top:0}
.plant{left:14px;top:62px;width:136px;height:100px;background:linear-gradient(135deg,#6f7a80,#b9c3c7 50%,#4e5a60)}
.about{position:absolute;left:14px;top:171px;width:138px}
.about p{margin-bottom:0}
.welder{left:164px;top:184px;width:122px;height:86px;background:radial-gradient(circle,#d7d0b8 0%,#6a6450 45%,#1e1e1c 100%)}
.benefit{position:absolute;left:164px;top:281px;width:124px}
.benefit h3{font-size:5.6px;font-weight:500;margin-bottom:4px;color:var(--ink)}
.benefit ul{list-style:none}
.benefit li{margin-bottom:2px}

/* panel 4 */
.col{position:absolute;top:8px}
.values{left:8px;width:134px}
.mission{left:158px;width:132px}
.col h2{font-size:11px;font-weight:500;color:var(--teal-dark);margin-bottom:5px}
.col h4{font-size:5.4px;font-weight:500;color:var(--teal-dark);margin:4px 0 2px}
.mission p{font-size:5.6px;line-height:1.38;font-weight:400;margin-bottom:6px;color:var(--ink)}
.mission h4{font-size:6.2px;font-weight:400}
.wave{position:absolute;left:0;bottom:0}
</style>
</head>
<body>
<div class="spread">

  <section class="panel panel-projects">
    <div class="ph map" role="img" aria-label="World map silhouette in teal showing global reach"></div>
    <h3 class="projects-title">A Selection of Some of our Recent Projects</h3>
    <ul class="projects">
      <li>In Australia, the commissioning of a 1,500 MW coal fired power station including turbine, generator and balance of plant control systems for the local utility and its operators.</li>
      <li>In New Zealand, the supply of electrical and instrumentation engineers for the upgrade of a hydro scheme with four 120 MW units and new excitation systems.</li>
      <li>In Malaysia, the installation and testing of a dynamic positioning and fuel gas system on board a floating production vessel operating offshore.</li>
      <li>In the UK, the electrical and control upgrade of a cable laying vessel including navigation bridge, alarm and monitoring systems for safe operation at sea.</li>
      <li>In Norway, the implementation and testing of load sharing and control systems for offshore power generation modules and gas compressors.</li>
      <li>In Peru, the commissioning of mining conveyors, crushers and substations supporting a new copper concentrator plant expansion in the highlands.</li>
      <li>In Bolivia, the supply of mechanical and piping supervisors for a gas processing plant including compressors, pumps and heat exchangers.</li>
      <li>In Indonesia, the mechanical installation of two gas turbine generator sets for an industrial power plant.</li>
    </ul>
    <div class="contact">
      <span class="h-teal">Our contact detail</span>
      Suite 12, Harbour Point Centre, 8 Quayside Road<br>
      &#9742; +00 555 0142 800<br>
      &#9993; consultancy@calm-meadowline.example<br>
      &#9679; www.calm-meadowline.example
    </div>
    <div class="badges"><span></span><span></span></div>
  </section>

  <section class="panel panel-cover">
    <div class="ph rig" role="img" aria-label="Photo of a yellow offshore oil platform on the open sea under a blue sky"></div>
    <div class="rule"></div>
    <ul class="services svc-a">
      <li>Automation Engineers</li>
      <li>Electrical Engineers</li>
      <li>Mechanical Engineers</li>
      <li>Telecom Engineers</li>
      <li>Civil Engineers</li>
    </ul>
    <ul class="services svc-b">
      <li>Hydraulics &amp; Pneumatics Engineers</li>
      <li>Piping Systems Fabrication</li>
      <li>Environmental Assessments &amp; Audits</li>
      <li>Marine Systems, Technical Services &amp; Solutions</li>
      <li>Occupational Health, Safety &amp; Environment Services<br>&nbsp;&nbsp;and Manpower</li>
    </ul>
    <div class="strip">
      <div class="s1" role="img" aria-label="Refinery towers at sunset"></div>
      <div class="s2" role="img" aria-label="Harbour cranes silhouetted at dusk"></div>
      <div class="s3" role="img" aria-label="Power transmission pylons at sunset"></div>
    </div>
    <div class="brand"><i></i><b>Calm Meadowline</b></div>
  </section>

  <section class="panel panel-about">
    <svg class="swoop" width="190" height="210" viewBox="0 0 190 210" aria-hidden="true">
      <path d="M40 0 H190 V150 C150 110 100 120 60 90 C30 68 30 30 40 0Z" fill="#3bb8c0"/>
      <path d="M20 0 C5 50 50 90 110 110 C150 125 175 160 190 190 V200 C170 160 140 135 95 122 C35 104 0 60 14 0Z" fill="#1f8e98"/>
      <path d="M0 78 C40 100 90 70 130 95 C160 113 180 150 190 170" stroke="#3bb8c0" stroke-width="3" fill="none"/>
    </svg>
    <div class="ph plant" role="img" aria-label="Photo of industrial machinery inside a plant"></div>
    <div class="about small">
      <p>Calm Meadowline was incorporated in October 2003. Our management consists of Electrical, Mechanical, Marine, Civil, Telecom and Geodetic Engineers from New Zealand, Australia, Sweden, Norway and the Philippines who have over 30 years of combined experiences.</p>
      <p>Known for its professionalism and corporate integrity, Calm Meadowline is committed to quality service and continual improvement and specializes in consultancy services, manpower services and technical services for maritime, offshore oil &amp; gas, power generation, mining, refineries and industrial plants world-wide.</p>
      <p>Calm Meadowline provides Technical Manpower and Consultancy Services deployable with minimal notice to any location globally; our team includes multi-lingual, multi-skilled and experienced personnel that have worked in some of the world's most challenging locations. Our consultants come from Australia, New Zealand, Philippines, India, Indonesia, Malaysia, Peru, Bolivia, UK, Sweden, Finland, Norway, Italy and Egypt.</p>
      <p>Past and current projects include mechanical and electrical installations, control systems upgrades, thermal and hydro power plant construction and commissioning, Marine Electronics, Control &amp; Alarm Systems and Navigation Bridge Systems. We pride ourselves on meeting our customers' needs and thrive on challenges. Our team will work hand in hand with your company to ensure your project is completed safely, on time and to the highest industry standards of quality.</p>
    </div>
    <div class="ph welder" role="img" aria-label="Photo of a technician working inside a large steel pipe"></div>
    <div class="benefit small">
      <h3>With Calm Meadowline, you benefit from:</h3>
      <ul>
        <li>• Contracted consultants on a contingent basis provides you with flexibility enabling a cost-effective approach to accommodate variability in demand and project cycles.</li>
        <li>• Our global pool of consultants enables us to provide an expert matching your specific needs, and reducing both delivery times and costs.</li>
        <li>• A single point of contact for consulting and contracting in multiple trades and skills enables you to focus on your core business.</li>
        <li>• Values, ethical approach to business providing courtesy and a corporate culture founded on honesty, integrity and professionalism.</li>
        <li>• Company founders with a strong track record in mining, civil, industrial, construction and power generation.</li>
      </ul>
    </div>
  </section>

  <section class="panel panel-values">
    <div class="col values small">
      <h2>Our Corporate Values</h2>
      <h4>Ethical behaviour and integrity:</h4>
      <p>Our foundation is our integrity, and all stakeholders are responsible for abiding by and upholding our Code of Business Conduct and Ethics. We are open and encourage all stakeholders to raise issues and discuss differences of opinion.</p>
      <p>We are honest and trustworthy in dealing with customers, suppliers, contractors, co-workers, shareholders and communities we affect.</p>
      <h4>Commitment to customers:</h4>
      <p>Our priority is to please our customers by providing the highest quality of services consistent with their requirements and specifications. We treat our customers fairly in all aspects of our business transactions. We strive to build strong and long term relationships with our customers and support their success by creating exceptional value through confidentiality, collaboration, continuous improvement and innovation.</p>
      <h4>Accountability:</h4>
      <p>We are accountable, individually and collectively, and take responsibility for our behaviours, actions and results, whether good or bad. We honour obligations, expectations and requirements, and deliver what we promised to deliver.</p>
      <h4>Commitment to personnel:</h4>
      <p>Our core is our personnel and we know that our success is based on their individual and collective contributions. We are honest in communications with our consultants and open in sharing information.</p>
      <p>We encourage our personnel in developing relevant and transferable skills. We promote an inclusive environment that fosters teamwork, trust, new ideas and equal opportunity to succeed, and we act on consultant suggestions and engage in good faith negotiations when conflict arises.</p>
    </div>
    <div class="col mission">
      <h2>Our Mission</h2>
      <h4>Purpose:</h4>
      <p>To provide qualified and motivated technical manpower and consultancy services to our clients worldwide.</p>
      <h4>Commitment:</h4>
      <p>We strive to exceed the needs and expectations of our clients through exemplary professional and technical services with continuous quality improvement.</p>
      <h4>Objective:</h4>
      <p>To continue building and maintaining our engineering team with the expertise for executing every project with success and total client satisfaction.</p>
      <h4>Vision:</h4>
      <p>To become the 'Industry' world leader in our sector through customer satisfaction.</p>
    </div>
    <svg class="wave" width="300" height="110" viewBox="0 0 300 110" aria-hidden="true">
      <path d="M90 110 C150 100 200 75 240 40 C262 20 282 8 300 4 V110Z" fill="#3bb8c0"/>
      <path d="M150 110 C200 98 240 80 270 55 C282 45 292 40 300 38 V110Z" fill="#1f8e98" opacity=".35"/>
    </svg>
  </section>

</div>
</body>
</html>
```